Bitcoin Wallet & NORA Landing Page

We need a landing page (one-pager) for our bitcoin wallet. we offer an online bitcoin wallet and an NORA prepaid card with which you can spend your bitcoins. Have similar offers: ledgerhop, zumi, monterra, kelpay Name will be: Coinlark

Industry/Entity Type

Online

Logo Text

Coinlark

Coding

Coded - Design and coding required

Number of Pages Required

1 page

Font styles to use
Sans Serif

Colors
3176b5
33a6d7

```html
<!DOCTYPE html>
<html lang="en">
<head>
<meta charset="utf-8">
<title>Coinlark – Bitcoin Wallet &amp; NORA Card</title>
<link href="https://fonts.googleapis.com/css2?family=Roboto:ital,wght@0,400;0,500;0,700;1,500;1,700&display=swap" rel="stylesheet">
<style>
:root{
  --brand:#3176b5;
  --sky:#33a6d7;
  --ink:#333;
  --white:#fff;
  --star:#e0a526;
}
*{box-sizing:border-box;margin:0;padding:0}
html,body{width:1200px;height:2469px;overflow:hidden}
body{font-family:'Roboto',Arial,sans-serif;color:var(--ink);background:var(--white);position:relative}
.abs{position:absolute}

/* header */
.site-header{top:0;left:0;width:1200px;height:143px;background:var(--white)}
.brand{display:flex;align-items:center;gap:14px;left:100px;top:36px}
.brand-mark{width:48px;height:48px;border-radius:50%;background:var(--brand);flex:none}
.brand-name{color:var(--brand);font-weight:700;font-size:30px;letter-spacing:1px}
.sign-in{left:998px;top:33px;width:104px;height:30px;border-radius:15px;background:var(--brand);color:var(--white);font-size:13px;font-weight:500;display:flex;align-items:center;justify-content:center;gap:8px}
.main-nav{top:96px;right:100px;display:flex;gap:44px;font-size:13px;font-weight:500;color:#222}
.main-nav .active{color:var(--brand)}

/* hero */
.hero{top:143px;left:0;width:1200px;height:581px;background:radial-gradient(circle at 60% 35%,#4a8fae 0%,#2f6f8e 40%,#1d4f6e 100%);text-align:center;color:var(--white)}
.hero h1{position:absolute;top:392px;width:100%;font-size:41px;font-weight:700;letter-spacing:.3px}
.hero p{position:absolute;top:462px;width:100%;font-size:21px;font-weight:500}

/* card section */
.card-section{top:724px;left:0;width:1200px;height:386px;background:var(--brand);color:var(--white)}
.card-section h2{position:absolute;left:98px;top:48px;font-size:30px;font-weight:500}
.card-list{position:absolute;left:98px;top:116px;list-style:none;font-size:12px}
.card-list li{height:34.5px;display:flex;align-items:flex-start;gap:20px}
.card-list li::before{content:"";width:7px;height:7px;border:2px solid var(--white);border-radius:50%;margin-top:2px;flex:none}
.card-visual{position:absolute;left:727px;top:36px;width:375px;height:350px;background:linear-gradient(100deg,#1f3f66 0%,#2a5c93 55%,#d9a52a 75%,#c28d1d 100%);border-radius:18px 18px 0 0}

/* wallet section */
.wallet-section{top:1110px;left:0;width:1200px;height:409px;background:linear-gradient(180deg,#33a6d7,#2b8cc4);color:var(--white);text-align:center}
.wallet-section h2{position:absolute;top:40px;width:100%;font-size:31px;font-weight:500}
.wallet-section h2 em{font-weight:700;font-style:italic}
.feature{position:absolute;top:120px;width:300px;text-align:center}
.feature svg{height:104px}
.feature h3{font-size:15px;font-weight:500;margin-top:22px}
.feature p{font-size:11.5px;line-height:24px;margin:12px auto 0;width:282px}

/* reviews */
.reviews{top:1519px;left:0;width:1200px;height:326px;background:linear-gradient(180deg,#ecebe9,#e4e1dc 60%,#efeeec);text-align:center}
.reviews h2{position:absolute;top:36px;width:100%;font-size:30px;font-weight:700;color:#3a3a3a}
.review{position:absolute;top:116px;width:320px}
.stars{color:var(--star);font-size:24px;letter-spacing:1px}
.review p{font-size:12.5px;line-height:20px;color:#444;margin-top:10px}
.review cite{display:block;font-style:normal;font-size:16px;color:#333;margin-top:18px}

/* partners */
.partners{top:1845px;left:0;width:1200px;height:223px;text-align:center}
.partners h2{position:absolute;top:35px;width:100%;font-size:29px;font-weight:700;color:#3a3a3a}
.partner-row{position:absolute;top:106px;left:99px;display:flex;gap:14px}
.partner{width:190px;height:64px;border:2px solid #eee;display:flex;align-items:center;justify-content:center}
.partner span{width:44px;height:30px;border-radius:6px;background:#bfbfbf}
.arrow{position:absolute;top:129px;font-size:22px;color:#aaa}

/* footer */
.site-footer{top:2068px;left:0;width:1200px;height:401px;background:linear-gradient(120deg,#353537,#232325 60%,#2d2d30);color:var(--white)}
.site-footer .brand{left:100px;top:80px}
.site-footer .brand-name{color:var(--white)}
.site-footer h4{font-size:17px;font-weight:700;position:absolute}
.newsletter{position:absolute;left:100px;top:248px;display:flex}
.newsletter input{width:196px;height:33px;border:0;padding-left:4px;font:11px 'Roboto',sans-serif}
.newsletter button{width:102px;height:33px;border:0;background:var(--brand);color:var(--white);font:700 13px 'Roboto',sans-serif}
.quick-links{position:absolute;left:448px;top:99px;list-style:none;font-size:12px;line-height:33px}
.contact-item,.social-item{position:absolute;display:flex;align-items:center;gap:24px;font-size:13px;line-height:19px}
.icon-dot{width:36px;height:36px;border-radius:50%;background:var(--white);display:flex;align-items:center;justify-content:center;flex:none}
.divider{position:absolute;left:100px;top:325px;width:1000px;height:1px;background:#555}
.copyright{position:absolute;top:355px;width:100%;text-align:center;font-size:12px}
</style>
</head>
<body>

<header class="site-header abs">
  <div class="brand abs"><span class="brand-mark"></span><span class="brand-name">COINLARK</span></div>
  <div class="sign-in abs">
    <svg width="12" height="12" viewBox="0 0 12 12"><path d="M1 5h6V3l3 3-3 3V7H1z" fill="#fff"/></svg>Sign In
  </div>
  <nav class="main-nav abs">
    <span class="active">Home</span><span>Bitcoin Credit Card</span><span>Bitcoin Wallaet</span><span>Customer Reviews</span><span>Partners</span>
  </nav>
</header>

<section class="hero abs" role="img" aria-label="Open hand beneath a glowing network of connected nodes and a bitcoin symbol">
  <h1>USE DIGITAL CURRENCY IN THE REAL WORLD</h1>
  <p>Nulla id neque eu dolor faucibus aliquam. Etiam non facilisis est.</p>
</section>

<section class="card-section abs">
  <h2>BITCOIN CREDIT CARD</h2>
  <ul class="card-list">
    <li>Lorem ipsum dolor sit amet, consectetur adipiscing elit.</li>
    <li>Vivamus ullamcorper, erat id viverra mollis, turpis lorem. Mollis elit, eget</li>
    <li>sodales libero arcu quis elit. Nullam eu nibh. Nullam non metus hendre-</li>
    <li>rit, dapibus lorem in.</li>
    <li>Aenean eget ex dapibus enim placerat congue.</li>
    <li>Maecenas pellentesque sem eu enim vehicula varius.</li>
  </ul>
  <div class="card-visual" role="img" aria-label="Smartphone showing a mobile banking app next to a gold prepaid card"></div>
</section>

<section class="wallet-section abs">
  <h2><em>THE SAFER</em>&nbsp; Bitcoin Wallet &nbsp;<em>THAT PUTS YOU IN CONTROL</em></h2>
  <div class="feature" style="left:108px">
    <svg viewBox="0 0 100 104"><path d="M50 4 90 18v30c0 26-18 44-40 52C28 92 10 74 10 48V18z" fill="none" stroke="#fff" stroke-width="6"/><rect x="34" y="48" width="32" height="26" rx="3" fill="#fff"/><path d="M40 48v-8a10 10 0 0 1 20 0v8" fill="none" stroke="#fff" stroke-width="5"/></svg>
    <h3>Improved Security</h3>
    <p>Pellentesque sed condimentum mi. Nulla vitae vulpu-tate tortor, vitae blandit. Vestibulum nisi ipsum, hen-drerit dictum venenatis</p>
  </div>
  <div class="feature" style="left:450px">
    <svg viewBox="0 0 110 104"><circle cx="46" cy="28" r="22" fill="#fff"/><path d="M4 100c0-28 18-44 42-44s30 8 34 14v30z" fill="#fff"/><circle cx="82" cy="78" r="24" fill="#fff" stroke="#2e95c9" stroke-width="4"/><rect x="72" y="76" width="20" height="15" rx="2" fill="#2e95c9"/><path d="M76 76v-5a6 6 0 0 1 12 0v5" fill="none" stroke="#2e95c9" stroke-width="3"/></svg>
    <h3>Quick Login</h3>
    <p>Pellentesque sed condimentum mi. Nulla vitae vulpu-tate tortor, vitae blandit. Vestibulum nisi ipsum, hen-drerit dictum venenatis</p>
  </div>
  <div class="feature" style="left:786px">
    <svg viewBox="0 0 100 104"><rect x="4" y="50" width="16" height="48" fill="#fff"/><path d="M24 54h30l18-10c8-4 14 4 8 10l-6 6h10c6 0 6 10 0 10h-8c6 0 6 10 0 10h-6c5 0 5 10 0 10H24z" fill="#fff"/><rect x="50" y="2" width="34" height="52" rx="3" fill="#fff" transform="rotate(12 67 28)"/><circle cx="67" cy="28" r="8" fill="#2e95c9"/></svg>
    <h3>Send Money Easily</h3>
    <p>Pellentesque sed condimentum mi. Nulla vitae vulpu-tate tortor, vitae blandit. Vestibulum nisi ipsum, hen-drerit dictum venenatis</p>
  </div>
</section>

<section class="reviews abs" role="img" aria-label="Faded group of smiling customers giving thumbs up behind the reviews">
  <h2>CUSTOMER REVIEWS</h2>
  <div class="review" style="left:98px"><div class="stars">★★★★★</div><p>Lorem ipsum dolor sit amet, consectetur adipiscing elit. Vestibulum quis semper arcu. Vivamus ullamcorper, erat id viverra mollis, turpis lorem mollis elit, eget sodales libero arcu quis elit</p><cite>- By Customer Name</cite></div>
  <div class="review" style="left:440px"><div class="stars">★★★★★</div><p>Lorem ipsum dolor sit amet, consectetur adipiscing elit. Vestibulum quis semper arcu. Vivamus ullamcorper, erat id viverra mollis, turpis lorem mollis elit, eget sodales libero arcu quis elit</p><cite>- By Customer Name</cite></div>
  <div class="review" style="left:776px"><div class="stars">★★★★★</div><p>Lorem ipsum dolor sit amet, consectetur adipiscing elit. Vestibulum quis semper arcu. Vivamus ullamcorper, erat id viverra mollis, turpis lorem mollis elit, eget sodales libero arcu quis elit</p><cite>- By Customer Name</cite></div>
</section>

<section class="partners abs">
  <h2>OUR PARTNERS</h2>
  <span class="arrow" style="left:52px">‹</span>
  <div class="partner-row">
    <div class="partner"><span></span></div>
    <div class="partner"><span></span></div>
    <div class="partner"><span></span></div>
    <div class="partner"><span></span></div>
    <div class="partner"><span></span></div>
  </div>
  <span class="arrow" style="left:1124px">›</span>
</section>

<footer class="site-footer abs">
  <div class="brand abs"><span class="brand-mark"></span><span class="brand-name">COINLARK</span></div>
  <h4 style="left:100px;top:204px">NEWSLETTER</h4>
  <form class="newsletter"><input type="text" placeholder="Enter Your Email..."><button type="button">SEND</button></form>

  <h4 style="left:448px;top:49px">QUICK LINKS</h4>
  <ul class="quick-links"><li>Home</li><li>Bitcoin Credit Card</li><li>Bitcoin Wallaet</li><li>Customer Reviews</li><li>Partners</li></ul>

  <h4 style="left:647px;top:49px">CONTACT US</h4>
  <div class="contact-item" style="left:641px;top:94px"><span class="icon-dot"><svg width="16" height="16" viewBox="0 0 16 16"><path d="M3 1l3 3-2 2c1 2 3 4 5 5l2-2 3 3-2 2C7 14 2 9 1 3z" fill="#333"/></svg></span>1-555-204-7310 | 1-555-204-7310</div>
  <div class="contact-item" style="left:641px;top:148px"><span class="icon-dot"><svg width="16" height="16" viewBox="0 0 16 16"><rect x="2" y="4" width="12" height="10" rx="1" fill="#333"/><rect x="5" y="1" width="6" height="4" fill="#333"/></svg></span>1-555-204-7311</div>
  <div class="contact-item" style="left:641px;top:208px;align-items:flex-start"><span class="icon-dot"><svg width="14" height="18" viewBox="0 0 14 18"><path d="M7 0a7 7 0 0 1 7 7c0 5-7 11-7 11S0 12 0 7a7 7 0 0 1 7-7z" fill="#333"/><circle cx="7" cy="7" r="2.5" fill="#fff"/></svg></span><span>18 Harbour Lark Lane<br>Brightwater, NL<br>B2C 4K7</span></div>

  <h4 style="left:962px;top:48px">FOLLOW US ON</h4>
  <div class="social-item" style="left:962px;top:93px;gap:16px"><span class="icon-dot"></span>Circlepost</div>
  <div class="social-item" style="left:962px;top:144px;gap:16px"><span class="icon-dot"></span>Friendwall</div>
  <div class="social-item" style="left:962px;top:195px;gap:16px"><span class="icon-dot"></span>Pinboardly</div>
  <div class="social-item" style="left:962px;top:246px;gap:16px"><span class="icon-dot"></span>Chirpnet</div>

  <div class="divider"></div>
  <p class="copyright">© Copyright 2017 - Coinlark . Allrights Reserved.</p>
</footer>

</body>
</html>
```